Real Estate Agent needs business card design

We have logo designed already, want to have business card designed. Very interested in those smaller size business card as they look very trendy. Business name is called VORENDA REALTY

```html
<!DOCTYPE html>
<html lang="en">
<head>
<meta charset="utf-8">
<title>Vorenda Realty – Business Card</title>
<link rel="stylesheet" href="https://fonts.googleapis.com/css2?family=Roboto:wght@400;500&family=Roboto+Condensed:wght@500;700&display=swap">
<style>
  :root {
    --backdrop: #e8e5e0;
    --card-black: #1b1c1e;
    --gold: #cba26a;
    --paper: #f3f3f3;
    --ink: #2b2b2b;
    --divider: #2e2e2e;
    --white: #ffffff;
  }
  * { box-sizing: border-box; margin: 0; padding: 0; }
  html, body {
    width: 1200px; height: 960px; overflow: hidden;
    background: var(--backdrop);
    font-family: "Roboto", Arial, sans-serif;
  }
  .canvas { position: relative; width: 1200px; height: 960px; }

  .card {
    position: absolute; left: 320px; width: 600px; height: 342px;
    border-radius: 22px; overflow: hidden;
    box-shadow: 0 4px 10px rgba(0,0,0,.25);
  }

  /* Front */
  .card-front { top: 108px; background: var(--card-black); }
  .front-brand {
    position: absolute; left: 0; right: 0; top: 150px;
    text-align: center; color: var(--gold);
    font-weight: 500; font-size: 34px; letter-spacing: 4px;
  }
  .front-web {
    position: absolute; left: 0; right: 0; bottom: 30px;
    text-align: center; color: var(--white);
    font-size: 14px; letter-spacing: 8px;
  }

  /* Back */
  .card-back { top: 493px; display: flex; }
  .contact-panel {
    width: 291px; background: var(--gold); color: var(--white);
    padding: 34px 0 0 34px; position: relative;
  }
  .divider { width: 6px; background: var(--divider); }
  .brand-panel {
    flex: 1; background: var(--paper);
    display: flex; flex-direction: column; align-items: center; justify-content: center;
    padding-top: 20px;
  }
  .person-name {
    font-family: "Roboto Condensed", Arial, sans-serif;
    font-weight: 700; font-size: 21px; line-height: 1.1;
  }
  .person-role {
    font-family: "Roboto Condensed", Arial, sans-serif;
    font-weight: 500; font-size: 15px; margin-top: 4px;
  }
  .address {
    position: absolute; left: 34px; top: 170px;
    font-size: 14.5px; line-height: 18px;
  }
  .contact-list {
    position: absolute; left: 34px; top: 216px; list-style: none;
    font-size: 14.5px; line-height: 19px;
  }
  .contact-list li { display: flex; align-items: center; gap: 8px; }
  .contact-list svg { width: 14px; height: 14px; fill: var(--white); flex: none; }

  .brand-mark { width: 26px; height: 26px; background: var(--gold); margin-bottom: 22px; }
  .brand-name {
    color: var(--ink); font-weight: 500; font-size: 28px; letter-spacing: 1.5px;
  }
</style>
</head>
<body>
<main class="canvas">

  <section class="card card-front" aria-label="Card front">
    <p class="front-brand">VORENDA REALTY</p>
    <p class="front-web">www.vorendarealty.com</p>
  </section>

  <section class="card card-back" aria-label="Card back">
    <div class="contact-panel">
      <h1 class="person-name">DANIEL HARTWELL</h1>
      <p class="person-role">CEO/FOUNDER</p>
      <p class="address">4120 Larkspur Court<br>Fairbanks, Alaska 99712</p>
      <ul class="contact-list">
        <li>
          <svg viewBox="0 0 16 16" aria-hidden="true"><path d="M3.2 1.5l2.3-.4 1.3 3.2-1.5 1.2a8.5 8.5 0 0 0 4.2 4.2l1.2-1.5 3.2 1.3-.4 2.3c-.2.9-1 1.4-1.9 1.3C6.3 12.6 3.4 9.7 1.9 4.4c-.1-.9.4-1.7 1.3-2.9z"/></svg>
          555 214 7830
        </li>
        <li>
          <svg viewBox="0 0 16 16" aria-hidden="true"><path d="M4.5 1h7a1 1 0 0 1 1 1v12a1 1 0 0 1-1 1h-7a1 1 0 0 1-1-1V2a1 1 0 0 1 1-1zm.8 1.8v9.4h5.4V2.8zM8 12.8a.8.8 0 1 0 0 1.6.8.8 0 0 0 0-1.6z"/></svg>
          555 381 6027
        </li>
        <li>
          <svg viewBox="0 0 16 16" aria-hidden="true"><path d="M4 1h8v4H4zM1.5 6h13a1 1 0 0 1 1 1v5h-3v3h-9v-3h-3V7a1 1 0 0 1 1-1zm3.5 5v2.5h6V11z"/></svg>
          555 902 4419
        </li>
        <li>
          <svg viewBox="0 0 16 16" aria-hidden="true"><path d="M1 4h14v9H1zm1.5 1.2v.3L8 9.2l5.5-3.7v-.3z"/></svg>
          daniel@vorendarealty.com
        </li>
        <li>
          <svg viewBox="0 0 16 16" aria-hidden="true"><path d="M8 1a7 7 0 1 0 0 14A7 7 0 0 0 8 1zm-1 2.3c-.8.9-1.7 1.6-2 2.8.7.6 1.7.4 2.3 1.1.6.8-.1 1.6.5 2.4.4.6.3 1.6.1 2.4A5.3 5.3 0 0 1 3 6.1c.9-1.5 2.3-2.5 4-2.8zm3.1.4A5.3 5.3 0 0 1 13 10c-.7-.5-1.5-.2-2-.9-.4-.7.3-1.6-.3-2.2-.7-.6-1.6.1-1.9-.9-.2-.8.7-1.4 1.3-2.3z"/></svg>
          www.vorendarealty.com
        </li>
      </ul>
    </div>
    <div class="divider"></div>
    <div class="brand-panel">
      <div class="brand-mark" aria-hidden="true"></div>
      <p class="brand-name">VORENDA REALTY</p>
    </div>
  </section>

</main>
</body>
</html>
```